Getränkefachhandel sucht Etiketten-Design für zwei Edelbrände
Zielgruppe
Wir sind ein Getränkefachhandel mit eigenen Getränkemärkten, dazu stellen wir Edelbrände her. Die Vermarktung läuft über unsere Getränkemärkte und die Gastronomie. Unsere bisherige Spirituosenlinie ist klassisch geprägt. In den letzten Monaten haben wir einen Gin mit abweichender Flasche und Design auf den Markt gebracht. Dies hat unsere Käuferschicht verjüngt. Deshalb wollen wir 2 klassische Edelbrände (Williams und Kirsch) in einer veränderten Qualität auf den markt bringen. Bilder sind beigefügt.
Aufgabenstellung
Keine besonderen Vorgaben. Das Design soll der neuen Gin-Linie angepasst werden und von der bisherigen Linie abweichen. Als Flasche wird nicht die klassische Longneckflasche, sondern die bauchige Ginflasche eingesetzt. Beide Flaschen haben 0,5 ltr. Inhalt. Es muss ein Feld für eine Losnummer, die bei der Abfüllung eingedruckt wird, vorbereitet werden. Die Produkte sind klassische Edelbrände mit Fruchtauszügen verfeinert, haben also eine goldgelbe (Williams) und rote (Kirsch) Farbe. Die Bezeichnungen lauten : Premium Williams Birne als Headliner und dem Zusatz Feine Spirituose mit Fruchtauszügen verfeinert, bzw. Premium Kirsche als Headliner und dem Zusatz Feine Spirituose mit Fruchtauszügen verfeinert. Evtl. können Fruchtbilder eingefügt werden. Vorgeschriebene Pflichtangaben sind : Inhalt 0,5 L und 37 % vol., sowie unsere Firmierung und Anschrift : Getränke Wolsink GmbH & Co. Brennerei und Mosterei KG, Lindauer Str. 31 - 33, 70327 Stuttgart. Diese Angaben können evtl. auch auf einem kleinen Zusatzetikett wie beim Gin angebracht werden. Ebenso die Losnummer. Die Deckelfarbe kann entweder in Holzoptik oder auch in Farbe gewählt werden.

```html
<!DOCTYPE html>
<html lang="de">
<head>
<meta charset="utf-8">
<title>Premium Kirsche &amp; Premium Williams Birne – Etiketten</title>
<link rel="stylesheet" href="https://fonts.googleapis.com/css2?family=Didact+Gothic&family=Petit+Formal+Script&display=swap">
<style>
  :root {
    --page: #ffffff;
    --label-bg: #ffffff;
    --label-edge: #d6d6d6;
    --ink: #1e1e1e;
    --ink-soft: #555555;
    --cherry: #e41f26;
    --pear: #8cc63f;
  }
  * { margin: 0; padding: 0; box-sizing: border-box; }
  html, body {
    width: 1085px; height: 1200px; overflow: hidden;
    background: var(--page);
  }
  .sheet {
    position: relative; width: 1085px; height: 1200px;
    font-family: "Didact Gothic", sans-serif; color: var(--ink);
  }
  .label {
    position: absolute; top: 301px;
    width: 490px; height: 597px;
    background: var(--label-bg);
    border: 1px solid var(--label-edge);
  }
  .label--kirsche { left: 35px; }
  .label--birne { left: 560px; }

  .label__premium {
    position: absolute; top: 72px; left: 0; width: 100%;
    text-align: center; font-size: 17px; letter-spacing: 0.55em;
    padding-left: 0.55em; line-height: 1;
  }
  .label__name {
    position: absolute; top: 95px; left: 0; width: 100%;
    text-align: center; font-size: 43px; line-height: 1;
    letter-spacing: -0.01em;
  }
  .label--kirsche .label__name { color: var(--cherry); }
  .label--birne .label__name { color: var(--pear); }

  .label__art { position: absolute; top: 153px; }
  .label--kirsche .label__art { left: 169px; width: 200px; height: 257px; }
  .label--birne .label__art { left: 100px; width: 324px; height: 247px; }

  .label__claim {
    position: absolute; top: 418px; left: 0; width: 100%;
    text-align: center; font-family: "Petit Formal Script", cursive;
    font-size: 16px; line-height: 25px; color: #333;
  }
  .label__abv {
    position: absolute; top: 520px; left: 70px;
    font-size: 27px; line-height: 1;
  }
  .label__abv small { font-size: 19px; }
  .label__volume {
    position: absolute; top: 520px; right: 76px;
    font-size: 27px; line-height: 1;
  }
  .label__web {
    position: absolute; top: 572px; left: 0; width: 100%;
    text-align: center; font-size: 12px; line-height: 1;
  }
  .label__motto {
    position: absolute; top: 24px; left: 6px; height: 550px;
    writing-mode: vertical-rl; font-size: 11.5px; line-height: 1;
    white-space: nowrap;
  }
  .label__maker {
    position: absolute; top: 24px; left: 470px; height: 550px;
    writing-mode: vertical-rl; transform: rotate(180deg);
    font-size: 11.5px; line-height: 1; white-space: nowrap;
  }
  .label__lot {
    position: absolute; top: 478px; left: 438px; height: 94px;
    writing-mode: vertical-rl; transform: rotate(180deg);
    font-size: 27px; letter-spacing: 0.12em; color: var(--ink-soft);
    line-height: 1;
  }
</style>
</head>
<body>
<main class="sheet">

  <section class="label label--kirsche">
    <p class="label__motto">Mit Liebe und Erfahrung aus besten Zutaten gebrannt für einen guten, wohlschmeckenden Tropfen</p>
    <p class="label__premium">PREMIUM</p>
    <h1 class="label__name">KIRSCHE</h1>
    <svg class="label__art" viewBox="0 0 200 257" role="img" aria-label="Mosaik-Buchstabe K in Rot- und Pinktönen mit zwei Kirschen">
      <defs>
        <linearGradient id="cherry-tone" x1="0" y1="0" x2="1" y2="1">
          <stop offset="0" stop-color="#f0386a"/>
          <stop offset="0.55" stop-color="#e41f26"/>
          <stop offset="1" stop-color="#8c1b24"/>
        </linearGradient>
      </defs>
      <rect width="200" height="257" fill="url(#cherry-tone)"/>
    </svg>
    <p class="label__claim">Feine Spirituose<br>mit Fruchtauszügen verfeinert</p>
    <p class="label__abv">37 % <small>Vol.</small></p>
    <p class="label__volume">0,5 L</p>
    <p class="label__lot">L0678</p>
    <p class="label__web">www.getraenke-wolsink.de</p>
    <p class="label__maker">Getränke Wolsink GmbH &amp; Co. Brennerei und Mosterei KG, Lindauer Str. 31 - 33, 70327 Stuttgart</p>
  </section>

  <section class="label label--birne">
    <p class="label__motto">Mit Liebe und Erfahrung aus besten Zutaten gebrannt für einen guten, wohlschmeckenden Tropfen</p>
    <p class="label__premium">PREMIUM</p>
    <h1 class="label__name">WILLIAMS BIRNE</h1>
    <svg class="label__art" viewBox="0 0 324 247" role="img" aria-label="Mosaik-Buchstabe W in Grüntönen mit zwei gelben Birnen">
      <defs>
        <linearGradient id="pear-tone" x1="0" y1="0" x2="1" y2="1">
          <stop offset="0" stop-color="#2d8a24"/>
          <stop offset="0.5" stop-color="#8cc63f"/>
          <stop offset="1" stop-color="#f4d65a"/>
        </linearGradient>
      </defs>
      <rect width="324" height="247" fill="url(#pear-tone)"/>
    </svg>
    <p class="label__claim">Feine Spirituose<br>mit Fruchtauszügen verfeinert</p>
    <p class="label__abv">37 % <small>Vol.</small></p>
    <p class="label__volume">0,5 L</p>
    <p class="label__lot">L0678</p>
    <p class="label__web">www.getraenke-wolsink.de</p>
    <p class="label__maker">Getränke Wolsink GmbH &amp; Co. Brennerei und Mosterei KG, Lindauer Str. 31 - 33, 70327 Stuttgart</p>
  </section>

</main>
</body>
</html>
```